Website for new dental office

I am Dr. Colin Marsh and am building a new dental practice. I specialize in general dentistry. I am young and have a higher end dental practice incorporating very new technologies and would like my website to reflect that. As many dental patients are older, the website must be very easy to navigate. I would like patients to be able to request appointments, and will eventually add on patient information forms (the health history, etc, that you normally fill out in the practice) from my practice management software, so leave an area for that.

Industry/Entity Type

Building

```html
<!DOCTYPE html>
<html lang="en">
<head>
<meta charset="utf-8">
<title>Marsh Dental Clinic</title>
<link href="https://fonts.googleapis.com/css2?family=Open+Sans:wght@400;600;700&display=swap" rel="stylesheet">
<style>
:root{
  --blue:#3aaedb;
  --blue-band:#4ab3de;
  --ink:#2b2b2b;
  --text:#555;
  --muted:#888;
  --line:#e3e3e3;
  --grey-band:#e5e5e5;
  --footer:#2a2a2a;
  --white:#fff;
}
*{margin:0;padding:0;box-sizing:border-box}
html,body{width:762px;height:1200px;overflow:hidden;background:var(--white)}
body{position:relative;font-family:"Open Sans",Arial,sans-serif;color:var(--text)}
h2,h3{font-weight:400}
.abs{position:absolute}

/* header */
.brand-dot{left:112px;top:14px;width:40px;height:40px;border-radius:50%;background:var(--blue)}
.brand-name{left:185px;top:25px;font-size:19px;font-weight:600;color:var(--blue);white-space:nowrap}
.social-top{left:437px;top:20px;display:flex;gap:7px}
.social-top span{width:10px;height:10px;border-radius:50%;background:#c4c4c4;display:block}
.search{left:535px;top:15px;width:119px;height:20px;border:1px solid #cfcfcf;border-radius:2px;font-size:7px;color:#aaa;padding:4px 6px}
.search svg{position:absolute;right:5px;top:4px}
.nav{left:378px;top:53px;width:275px;display:flex;justify-content:space-between;font-size:6.2px;font-weight:600;color:#444;white-space:nowrap}
.nav .active{color:var(--blue)}

/* hero */
.hero{left:0;top:80px;width:762px;height:338px;background:linear-gradient(90deg,#dcdcdc 0%,#efefef 35%,#e6e8e8 60%,#cfcfcf 100%)}
.hero-caption{left:264px;top:184px;min-width:234px;height:64px;background:rgba(60,60,60,.85);color:var(--white);font-size:15.5px;line-height:24px;padding:8px 12px;white-space:nowrap}
.hero-arrow{top:231px;width:18px;height:18px;border-radius:50%;background:rgba(255,255,255,.7);border:1px solid #ccc}

/* services */
.services{left:110px;top:349px;width:543px;height:174px;background:var(--blue-band);display:flex;box-shadow:0 4px 6px rgba(0,0,0,.12)}
.service{flex:1;text-align:center;color:var(--white);padding-top:22px;border-right:1px solid rgba(255,255,255,.2)}
.service:last-child{border-right:0}
.service-icon{width:72px;height:72px;border-radius:50%;background:var(--white);border:3px solid #d8eef7;margin:0 auto;display:flex;align-items:center;justify-content:center}
.service h3{font-size:10px;margin-top:10px}
.service p{font-size:7.2px;line-height:13px;margin:5px auto 0;width:150px}

/* welcome */
.welcome-img{left:110px;top:548px;width:173px;height:138px;border:1px solid var(--line);padding:3px}
.welcome-img div{width:100%;height:100%;background:linear-gradient(135deg,#f4f4f4,#e2e2e2 70%,#f0d0c8)}
.welcome-title{left:309px;top:545px;font-size:13px;color:var(--ink)}
.welcome-title span{color:var(--blue)}
.welcome-text{left:307px;top:573px;width:346px;font-size:6.2px;line-height:12px;text-align:justify;color:#666}
.welcome-text p+p{margin-top:6px}
.btn{left:307px;top:661px;width:54px;height:24px;background:var(--footer);color:var(--white);font-size:7px;font-weight:600;border-radius:3px;display:flex;align-items:center;justify-content:center}

/* appointment */
.appt{left:110px;top:707px;width:292px;height:192px;border:1px solid var(--line)}
.appt-photo{left:110px;top:720px;width:154px;height:179px;background:linear-gradient(180deg,#f3ece2,#e9eef2 60%,#9ec7cf)}
.appt-title{left:261px;top:722px;font-size:16px;color:var(--ink);line-height:24px}
.appt-title strong{display:block;font-size:21px;font-weight:400;color:var(--blue)}
.appt-desc{left:261px;top:784px;width:130px;font-size:6.2px;line-height:12px;color:#555}
.appt-row{left:264px;font-size:8.5px;color:var(--ink);display:flex;align-items:center;gap:11px}
.appt-go{left:367px;top:869px;width:18px;height:18px;border:1.5px solid var(--blue);border-radius:50%}

/* centers */
.centers-bar{left:419px;top:707px;width:234px;height:26px;background:var(--blue-band);color:var(--white);font-size:12.5px;padding:4px 9px}
.center-img{width:88px;height:68px;border:1px solid var(--line);padding:2px}
.center-img div{width:100%;height:100%;background:linear-gradient(135deg,#b9d3de,#f0e6dc 60%,#d8dde0)}
.center-title{left:520px;font-size:9.5px;color:var(--ink)}
.center-text{left:520px;width:133px;font-size:6px;line-height:12px;text-align:justify;color:#555}
.center-more{left:520px;font-size:6px;color:var(--blue)}

/* technologies */
.tech-band{left:0;top:926px;width:762px;height:209px;background:var(--grey-band)}
.tech-title{left:111px;top:945px;font-size:10px;color:var(--blue)}
.tech-nav{left:623px;top:944px;display:flex}
.tech-nav span{width:16px;height:16px;border:1px solid #ccc;background:#f4f4f4;font-size:7px;color:#999;display:flex;align-items:center;justify-content:center}
.tech-card{top:973px;width:129px;height:137px;border:1px solid #d0d0d0;background:var(--white)}
.tech-card .img{height:108px}
.tech-card .cap{height:28px;background:#3a3a3a;color:var(--white);font-size:9.5px;font-weight:600;display:flex;align-items:center;justify-content:center}

/* footer */
.footer{left:0;top:1135px;width:762px;height:65px;background:var(--footer);border-top:3px solid var(--blue)}
.foot-links{left:109px;top:1152px;font-size:6.5px;color:#ddd;word-spacing:2px}
.foot-copy{left:109px;top:1172px;font-size:6.2px;color:#bbb}
.foot-social{left:558px;top:1153px;display:flex;gap:8px}
.foot-social span{width:18px;height:18px;border-radius:50%;display:block;border:2px solid #555}
</style>
</head>
<body>

<header>
  <div class="abs brand-dot"></div>
  <div class="abs brand-name">Marsh Dental Clinic</div>
  <div class="abs social-top"><span></span><span></span><span></span><span></span><span></span><span></span></div>
  <div class="abs search">Search
    <svg width="10" height="10" viewBox="0 0 10 10"><circle cx="4" cy="4" r="3" fill="none" stroke="#3aaedb" stroke-width="1.3"/><line x1="6.2" y1="6.2" x2="9.2" y2="9.2" stroke="#3aaedb" stroke-width="1.5"/></svg>
  </div>
  <nav class="abs nav">
    <span class="active">ABOUT US</span><span>SERVICES</span><span>PATIENTS</span><span>PROFESSIONALS</span><span>BLOG</span><span>CONTACT</span>
  </nav>
</header>

<section>
  <div class="abs hero" role="img" aria-label="Photo of smiling dentists with a young patient in a bright clinic"></div>
  <div class="abs hero-caption">Dr. Colin Marsh is specialised<br>in general dentistry</div>
  <div class="abs hero-arrow" style="left:43px"></div>
  <div class="abs hero-arrow" style="left:701px"></div>
</section>

<section class="abs services">
  <div class="service">
    <div class="service-icon">
      <svg width="26" height="22" viewBox="0 0 26 22"><rect x="1" y="5" width="24" height="16" rx="2" fill="#888"/><rect x="9" y="1" width="8" height="5" rx="1" fill="none" stroke="#888" stroke-width="2"/><rect x="11.5" y="8" width="3" height="10" fill="#fff"/><rect x="8" y="11.5" width="10" height="3" fill="#fff"/></svg>
    </div>
    <h3>EMERGENCY</h3>
    <p>Lorem Ipsum is simply dummy Lorem Ipsum has been the industry's standard dummy text..</p>
  </div>
  <div class="service">
    <div class="service-icon">
      <svg width="24" height="26" viewBox="0 0 24 26"><line x1="5" y1="24" x2="17" y2="3" stroke="#888" stroke-width="3" stroke-linecap="round"/><line x1="11" y1="24" x2="20" y2="7" stroke="#888" stroke-width="2" stroke-linecap="round"/></svg>
    </div>
    <h3>CARE ADVICE</h3>
    <p>Lorem Ipsum is simply dummy Lorem Ipsum has been the industry's standard dummy text..</p>
  </div>
  <div class="service">
    <div class="service-icon">
      <svg width="24" height="28" viewBox="0 0 24 28"><path d="M2 10 L12 2 L22 10 V26 H2 Z" fill="none" stroke="#888" stroke-width="2"/><path d="M8 13 C8 11 11 11 12 12 C13 11 16 11 16 13 C16 16 15 22 14 22 C13 22 13 18 12 18 C11 18 11 22 10 22 C9 22 8 16 8 13 Z" fill="#888"/></svg>
    </div>
    <h3>VIP SERVICES</h3>
    <p>Lorem Ipsum is simply dummy Lorem Ipsum has been the industry's standard dummy text..</p>
  </div>
</section>

<section>
  <div class="abs welcome-img"><div role="img" aria-label="Photo of a dental prosthesis on a white surface"></div></div>
  <h2 class="abs welcome-title">Welcome To <span>Marsh Dental Clinic</span></h2>
  <div class="abs welcome-text">
    <p>Etiam quis mi ante. Donec iaculis ornare enim non dapibus. Vivamus ac nisi eros. Nam non commodo mi. Pellentesque habitant morbi tristique senectus et netus et malesuada fames ac turpis egestas.Etiam quis mi ante. Donec iaculis ornare enim non dapibus. Vivamus ac nisi eros. Nam non commodo mi. Pellentesque habitant morbi tristique senectus et netus et malesuada fames ac turpis egestas.</p>
    <p>Etiam quis mi ante. Donec iaculis ornare enim non dapibus. Vivamus ac nisi eros. Nam non commodo mi. Pellentesque habitant morbi tristique senectus et netus et malesuada fames ac turpis egestas.</p>
  </div>
  <div class="abs btn">Read More</div>
</section>

<section>
  <div class="abs appt"></div>
  <div class="abs appt-photo" role="img" aria-label="Photo of a smiling doctor with a stethoscope giving a thumbs up"></div>
  <h2 class="abs appt-title">Make an<strong>Appointment</strong></h2>
  <p class="abs appt-desc">Quisque nulla. Vestibulum porta vel, scelerisque eget, malesuada at, neque.</p>
  <div class="abs appt-row" style="top:824px">
    <svg width="12" height="10" viewBox="0 0 12 10"><path d="M1 3 C1 1 11 1 11 3 L9 4 L8 3 H4 L3 4 Z" fill="#222"/><rect x="2.5" y="5" width="7" height="4.5" rx="1" fill="#222"/></svg>
    <span>(555) 014-2290</span>
  </div>
  <div class="abs appt-row" style="top:844px">
    <svg width="12" height="9" viewBox="0 0 12 9"><rect x="0.5" y="0.5" width="11" height="8" fill="#222"/><path d="M0.5 0.5 L6 5 L11.5 0.5" fill="none" stroke="#fff" stroke-width="1"/></svg>
    <span>info@marshdentalclinic.com</span>
  </div>
  <div class="abs appt-go">
    <svg width="15" height="15" viewBox="0 0 15 15"><path d="M4 7.5 H11 M8 4.5 L11 7.5 L8 10.5" fill="none" stroke="#3aaedb" stroke-width="1.4"/></svg>
  </div>
</section>

<section>
  <div class="abs centers-bar">Notable Centers Of Excellence</div>
  <div class="abs center-img" style="left:421px;top:748px"><div role="img" aria-label="Photo of a smiling dental assistant in a treatment room"></div></div>
  <h3 class="abs center-title" style="top:747px">Class aptent taciti sociosqu</h3>
  <p class="abs center-text" style="top:767px">Lorem ipsum dolor sit amet, consectetuer adipiscing elit, sed diam nonummy nibh euismod tincidunt</p>
  <span class="abs center-more" style="top:810px">Read More</span>

  <div class="abs center-img" style="left:421px;top:830px"><div role="img" aria-label="Photo of a dental assistant smiling beside a dental chair"></div></div>
  <h3 class="abs center-title" style="top:829px;left:523px">Dental assistant smiling</h3>
  <p class="abs center-text" style="top:849px">Lorem ipsum dolor sit amet, consectetuer adipiscing elit, sed diam nonummy nibh euismod tincidunt</p>
  <span class="abs center-more" style="top:892px">Read More</span>
</section>

<section>
  <div class="abs tech-band"></div>
  <h2 class="abs tech-title">New Technologies</h2>
  <div class="abs tech-nav"><span>&lsaquo;</span><span>&rsaquo;</span></div>
  <div class="abs tech-card" style="left:111px"><div class="img" role="img" aria-label="Photo of an operating room with surgical lamps" style="background:linear-gradient(180deg,#c9d7e0,#8fb2c4 60%,#4fb0b0)"></div><div class="cap">Rolernatur aut oditaut</div></div>
  <div class="abs tech-card" style="left:248px"><div class="img" role="img" aria-label="Photo of a medical monitor on a stand" style="background:linear-gradient(180deg,#e4e6e8,#cdd2d4 60%,#2aa79a)"></div><div class="cap">Dolores miertyas eses</div></div>
  <div class="abs tech-card" style="left:387px"><div class="img" role="img" aria-label="Photo of a modern dental chair" style="background:linear-gradient(135deg,#eeeeee,#d9d9d9 50%,#8e2a3e)"></div><div class="cap">Ferrode mias lertyera</div></div>
  <div class="abs tech-card" style="left:527px"><div class="img" role="img" aria-label="Photo of a bright recovery ward with beds" style="background:linear-gradient(180deg,#e6ebe8,#c8dce0 55%,#6fc4d4)"></div><div class="cap">Estqui dolorem ipsum</div></div>
</section>

<footer>
  <div class="abs footer"></div>
  <div class="abs foot-links">HOME &nbsp;| ABOUT US | SERVICES | PATIENTS | PROFESSIONALS | BLOG | CONTACT</div>
  <div class="abs foot-copy">©2014 Marsh Dental Clinic, All Rights Reserved.</div>
  <div class="abs foot-social">
    <span style="background:#2fa9e0"></span><span style="background:#3b5bab"></span><span style="background:#666"></span><span style="background:#e0457b"></span>
  </div>
</footer>

</body>
</html>
```